4D Hush Little Nest Luxury Ultrasound Billboard

Design a HIGH-END, MODERN billboard for my private prenatal ultrasound studio, 4D Hush Little Nest, located in Pace, Florida.
This billboard will be viewed by drivers traveling at highway speeds, so it must be extremely clean, simple, and readable within 6 seconds.
About My Business
4D Hush Little Nest is a private prenatal ultrasound studio specializing in:
Highest technology 4D/HD Ultrasounds
Early Gender Determination
Pregnancy Confirmation
I have been serving families for nearly 10 years and is known for creating a memorable experience, not just an ultrasound appointment.
Design Style
I DO NOT want:
Flowers
Leaves
Swirls
Glitter
Hearts everywhere
Busy backgrounds
Generic maternity stock graphics
I DO want:
Modern
Luxury
Upscale
Clean
Professional
Eye-catching
Premium medical spa feel
Colors
Use colors from my logo:
LOGO Green ( or a deep green)
Black
White
Soft Gold accents
Images:
Incorporate my professional headshot in a clean, modern way, logo, and the ultrasound images
Text
Keep wording minimal.
Primary Headline ( OPEN TO IDEAS) :
EXAMPLES ( WOULD RATHER SOMETHING MORE CATCHY)
" ADVANCED IMAGING. UNFORGETTABLE MOMENTS"
"MEET YOUR BABY BEFORE BIRTH"
Under headline:
4D Ultrasound • Early Gender • Pregnancy Confirmation
Business Name:
4D Hush Little Nest
Private Prenatal Ultrasound Studio
Phone Number:
850-471-3905
Important
This billboard must be readable in 5–6 seconds from a moving vehicle.
Less text is better.
The phone number and business name must be visible from a distance.
The design should feel like a premium brand that immediately tells expecting parents:
“This is where I go to see my baby.”
Files Provided
Official logo
Headshot
Ultrasound images
Don’t make this look like a medical office billboard.
Make it look like a luxury baby experience billboard. That’s what separates 4D Hush Little Nest from hospitals, OB offices, and all the new studios popping up around you. The emotional connection is what gets moms to book. ❤️
Billboard Size - 10.6” x 36”

```html
<!DOCTYPE html>
<html lang="en">
<head>
<meta charset="utf-8">
<title>4D Hush Little Nest Billboard</title>
<link rel="stylesheet" href="https://fonts.googleapis.com/css2?family=Cinzel:wght@500&family=Kaushan+Script&family=Poppins:wght@400;700&display=swap">
<style>
  :root {
    --green: #4a5a4e;
    --green-deep: #3f4d43;
    --gold: #b8923a;
    --white: #f6f5f1;
    --black: #1b1c1d;
    --page: #e9ebee;
    --tape: #e6d3a7;
  }
  html, body {
    margin: 0;
    width: 1200px;
    height: 998px;
    overflow: hidden;
    background: var(--page);
  }
  .billboard {
    position: absolute;
    left: 0;
    top: 322px;
    width: 1200px;
    height: 353px;
    background: linear-gradient(90deg, var(--green-deep), var(--green) 40%, var(--green));
    overflow: hidden;
  }
  .headshot {
    position: absolute;
    left: 0;
    top: 0;
    width: 215px;
    height: 353px;
    background: linear-gradient(90deg, #d9d8d4 0%, #c7b9a0 45%, #6b735f 80%, var(--green-deep) 100%);
  }
  .bottom-wave {
    position: absolute;
    left: 0;
    top: 0;
    width: 1200px;
    height: 353px;
  }
  .brand-tab {
    position: absolute;
    left: 505px;
    top: 0;
    width: 160px;
    height: 92px;
    background: var(--white);
    border-radius: 0 0 10px 10px;
    display: flex;
    align-items: center;
    justify-content: center;
    text-align: center;
  }
  .brand-name {
    font-family: "Poppins", sans-serif;
    font-weight: 700;
    font-size: 17px;
    line-height: 1.2;
    color: var(--gold);
    margin: 0 12px;
  }
  .headline {
    position: absolute;
    left: 300px;
    top: 100px;
    width: 620px;
    margin: 0;
    text-align: center;
    font-family: "Cinzel", serif;
    font-weight: 500;
    font-size: 60px;
    letter-spacing: 1px;
    color: var(--white);
    line-height: 1;
  }
  .headline-script {
    position: absolute;
    left: 380px;
    top: 158px;
    width: 460px;
    text-align: center;
    font-family: "Kaushan Script", cursive;
    font-size: 54px;
    color: var(--gold);
    line-height: 1;
  }
  .services {
    position: absolute;
    left: 280px;
    top: 220px;
    width: 660px;
    margin: 0;
    text-align: center;
    font-family: "Poppins", sans-serif;
    font-size: 15px;
    line-height: 22px;
    letter-spacing: 1.5px;
    color: var(--white);
    white-space: nowrap;
  }
  .services .divider {
    color: var(--gold);
    margin: 0 10px;
  }
  .phone {
    position: absolute;
    left: 430px;
    top: 286px;
    width: 360px;
    display: flex;
    align-items: center;
    justify-content: center;
    gap: 10px;
    font-family: "Poppins", sans-serif;
    font-weight: 700;
    font-size: 30px;
    letter-spacing: 1px;
    color: var(--green-deep);
  }
  .scan-frame {
    position: absolute;
    left: 960px;
    top: 34px;
    width: 180px;
    height: 180px;
    background: var(--black);
    padding: 14px;
    box-sizing: border-box;
  }
  .scan-image {
    width: 100%;
    height: 100%;
    background: radial-gradient(circle at 35% 45%, #b2604c, #7a3527 60%, #3a1a15);
  }
  .tape {
    position: absolute;
    width: 56px;
    height: 13px;
    background: var(--tape);
    opacity: 0.9;
  }
  .tape-top { left: 944px; top: 40px; transform: rotate(-40deg); }
  .tape-bottom { left: 1106px; top: 198px; transform: rotate(-40deg); }
</style>
</head>
<body>
  <div class="billboard">
    <div class="headshot" role="img" aria-label="Professional headshot of the studio owner holding an ultrasound probe"></div>

    <svg class="bottom-wave" viewBox="0 0 1200 353" aria-hidden="true">
      <path d="M0,312 C200,322 360,292 460,272 C560,254 700,258 820,258 C960,258 1080,200 1200,150 L1200,180 C1080,228 960,272 820,272 C700,272 560,270 460,288 C360,308 200,336 0,330 Z" fill="var(--gold)"/>
      <path d="M0,330 C200,336 360,308 460,288 C560,270 700,272 820,272 C960,272 1080,228 1200,180 L1200,353 L0,353 Z" fill="var(--white)"/>
    </svg>

    <div class="brand-tab">
      <span class="brand-name">4D Hush Little Nest</span>
    </div>

    <h1 class="headline">MEET YOUR BABY</h1>
    <div class="headline-script">Before Birth</div>

    <p class="services">4D Ultrasound<span class="divider">|</span>Early Gender<span class="divider">|</span>Pregnancy Confirmation</p>

    <div class="phone">
      <svg width="18" height="22" viewBox="0 0 24 24" aria-hidden="true">
        <path d="M6.6 10.8c1.4 2.8 3.8 5.1 6.6 6.6l2.2-2.2c.3-.3.7-.4 1-.2 1.1.4 2.3.6 3.6.6.6 0 1 .4 1 1V20c0 .6-.4 1-1 1C10.6 21 3 13.4 3 4c0-.6.4-1 1-1h3.5c.6 0 1 .4 1 1 0 1.3.2 2.5.6 3.6.1.3 0 .7-.2 1L6.6 10.8z" fill="var(--gold)"/>
      </svg>
      <span>850-471-3905</span>
    </div>

    <div class="scan-frame">
      <div class="scan-image" role="img" aria-label="4D ultrasound image of twin babies face to face"></div>
    </div>
    <div class="tape tape-top"></div>
    <div class="tape tape-bottom"></div>
  </div>
</body>
</html>
```